" Uma empresa que funcionará em sua maior parte para o B2B ,onde motoristas que não tem veículos para trabalhar,contratam para ir ao mercado de trabalho e alugar frotas pra empresas "

```html
<!DOCTYPE html>
<html lang="pt-BR">
<head>
<meta charset="utf-8">
<title>Rovia Locadora de Veículos — Papelaria</title>
<link rel="stylesheet" href="https://fonts.googleapis.com/css2?family=Nunito:wght@400;600;800&display=swap">
<style>
  :root {
    --teal: #1e98b5;
    --teal-dark: #127f9c;
    --teal-light: #33b3cf;
    --teal-mist: rgba(42, 163, 192, 0.22);
    --paper: #ffffff;
    --paper-soft: #eef1f2;
    --ink-soft: #6f7a80;
    --stage: #e6e9eb;
  }
  * { margin: 0; padding: 0; box-sizing: border-box; }
  html, body { width: 1200px; height: 1200px; overflow: hidden; }
  body {
    background: var(--stage);
    font-family: "Nunito", sans-serif;
    position: relative;
  }

  /* Front card */
  .card-front {
    position: absolute;
    left: 144px; top: 156px;
    width: 912px; height: 444px;
    background: var(--paper);
  }
  .wave-band {
    position: absolute;
    left: 0; right: 0; top: 30px;
    height: 200px;
    background: linear-gradient(180deg, rgba(42,163,192,0) 0%, var(--teal-mist) 50%, rgba(42,163,192,0) 100%);
  }
  .brand {
    display: flex;
    flex-direction: column;
  }
  .brand-row {
    display: flex;
    align-items: center;
    gap: 12px;
  }
  .brand-mark {
    border-radius: 50%;
    flex: none;
  }
  .brand-name {
    font-weight: 800;
    line-height: 1;
    letter-spacing: -1px;
  }
  .brand-tagline {
    font-weight: 800;
    text-transform: uppercase;
    letter-spacing: 0.3px;
    white-space: nowrap;
  }

  .brand-front {
    position: absolute;
    right: 96px; top: 268px;
    align-items: flex-end;
    color: var(--teal);
  }
  .brand-front .brand-mark { width: 26px; height: 26px; background: var(--teal); }
  .brand-front .brand-name { font-size: 96px; }
  .brand-front .brand-tagline { font-size: 20px; margin-top: 2px; }

  /* Envelope back */
  .envelope-back {
    position: absolute;
    left: 144px; top: 644px;
    width: 912px; height: 480px;
    background: var(--paper-soft);
    overflow: hidden;
  }
  .envelope-back .flap { position: absolute; left: 0; top: 0; width: 912px; height: 280px; }
  .brand-back {
    position: absolute;
    left: 0; right: 0; top: 120px;
    align-items: center;
    color: var(--paper);
  }
  .brand-back .brand-mark { width: 18px; height: 18px; background: var(--paper); }
  .brand-back .brand-name { font-size: 68px; }
  .brand-back .brand-tagline { font-size: 15px; margin-top: 0; }

  .contact-list {
    position: absolute;
    left: 52px; top: 302px;
    list-style: none;
    color: var(--ink-soft);
    font-size: 14px;
    font-weight: 600;
  }
  .contact-list li {
    display: flex;
    align-items: center;
    gap: 10px;
    height: 24px;
  }
  .contact-list svg { width: 12px; height: 12px; flex: none; }
</style>
</head>
<body>

<section class="card-front">
  <div class="wave-band" role="img" aria-label="Faixa decorativa de linhas onduladas em azul-petróleo"></div>
  <div class="brand brand-front">
    <div class="brand-row">
      <span class="brand-mark"></span>
      <span class="brand-name">rovia</span>
    </div>
    <div class="brand-tagline">Locadora de Veículos</div>
  </div>
</section>

<section class="envelope-back">
  <svg class="flap" viewBox="0 0 912 280">
    <defs>
      <linearGradient id="flapFill" x1="0" y1="0" x2="0" y2="1">
        <stop offset="0" stop-color="var(--teal-light)"/>
        <stop offset="1" stop-color="var(--teal-dark)"/>
      </linearGradient>
    </defs>
    <path d="M0 0 H912 V215 C912 252 886 272 850 272 H62 C26 272 0 252 0 215 Z" fill="url(#flapFill)"/>
  </svg>
  <div class="brand brand-back">
    <div class="brand-row">
      <span class="brand-mark"></span>
      <span class="brand-name">rovia</span>
    </div>
    <div class="brand-tagline">Locadora de Veículos</div>
  </div>

  <ul class="contact-list">
    <li>
      <svg viewBox="0 0 12 12"><path d="M6 0.5a4 4 0 0 0-4 4c0 3 4 7 4 7s4-4 4-7a4 4 0 0 0-4-4z" fill="var(--ink-soft)"/><circle cx="6" cy="4.5" r="1.4" fill="var(--paper-soft)"/></svg>
      Rua das Frotas, 480 • Vila Motora • Campo Alto • SP
    </li>
    <li>
      <svg viewBox="0 0 12 12"><path d="M2.5 1h2l1 2.6-1.3 1a6 6 0 0 0 3.2 3.2l1-1.3 2.6 1v2a1 1 0 0 1-1 1A9.5 9.5 0 0 1 1.5 2a1 1 0 0 1 1-1z" fill="var(--ink-soft)"/></svg>
      (11) 4820-7316
    </li>
    <li>
      <svg viewBox="0 0 12 12" fill="none" stroke="var(--ink-soft)" stroke-width="1.3"><rect x="1" y="2.5" width="10" height="7" rx="1"/><path d="M1 3l5 3.5L11 3"/></svg>
      contato@rovialocadora.com.br
    </li>
    <li>
      <svg viewBox="0 0 12 12"><circle cx="6" cy="6" r="5" fill="var(--ink-soft)"/></svg>
      @rovialocadora
    </li>
    <li>
      <svg viewBox="0 0 12 12" fill="none" stroke="var(--ink-soft)" stroke-width="1.2"><circle cx="6" cy="6" r="5"/><ellipse cx="6" cy="6" rx="2.2" ry="5"/><path d="M1 6h10"/></svg>
      www.rovialocadora.com.br
    </li>
  </ul>
</section>

</body>
</html>
```